Tavrel Crafted Interiors logo and business card

Tavrel is a female operated furniture design and reupholstery business. Working with luxury top end fabrics and furnishings for unique and stylish one off designs. Bringing loved pieces of furniture back to life by recovering on modern, trendy, stylish fabrics. Think Velvet chaise lounge or velour Chesterfield lounges, vibrant and unique colourful, individually designed statement pieces.
We would like a simple logo that can be used on socials and a business card that is simple yet striking . Possibly using a bronze or gold foil.
The business name is TAVREL CRAFTED INTERIORS
Can be just TAVREL
Logo will be used on socials and images of finished furniture.

Target Market(s)

high end luxury holiday houses. Artistic flair designer houses

Industry/Entity Type

Home Furniture

Contact Information for Business Card

Simple yet designer
Logo on the front and name details on the back

Font styles to use
Decorative

Requirements
Must have
• Finess
A feel of artistic design
Just a logo/business name on the front of the card
Should not have
• not a picture of furniture

```html
<!DOCTYPE html>
<html lang="en">
<head>
<meta charset="utf-8">
<title>Tavrel Crafted Interiors – Business Card</title>
<link rel="stylesheet" href="https://fonts.googleapis.com/css2?family=Arimo:wght@400&family=Cinzel:wght@400;700&family=Montserrat:wght@600&display=swap">
<style>
  :root {
    --backdrop: #0d0d0e;
    --card: #2a2a2d;
    --card-back: #262628;
    --foil: #c9a063;
    --foil-edge: #b08848;
    --foil-deep: #7a5a2c;
    --text: #d9d9dc;
    --muted: #b9b9be;
    --emboss: #4a4a4e;
    --rule: #55555a;
  }
  * { box-sizing: border-box; margin: 0; padding: 0; }
  html, body {
    width: 1200px; height: 820px; overflow: hidden;
    background: var(--backdrop);
  }
  .canvas {
    width: 1200px; height: 820px;
    display: flex; align-items: center; justify-content: center; gap: 60px;
    background: radial-gradient(ellipse at 50% 45%, #1a1a1c 0%, var(--backdrop) 70%);
  }
  .card {
    position: relative;
    width: 525px; height: 300px;
    border-radius: 3px;
  }
  .card--front {
    background: var(--card);
    border-left: 2px solid var(--foil);
    border-bottom: 2px solid var(--foil);
  }
  .card--back {
    background: var(--card-back);
    box-shadow: 3px 3px 0 var(--foil-edge), 5px 5px 0 var(--foil-deep), 7px 7px 0 var(--foil-edge);
    display: flex; align-items: center; justify-content: center;
  }
  .brand {
    font-family: "Cinzel", serif;
    text-align: center;
    line-height: 1;
  }
  .brand__name { font-weight: 700; font-size: 60px; letter-spacing: 7px; }
  .brand__tagline { font-weight: 400; font-size: 15px; letter-spacing: 4px; margin-top: 10px; }
  .card--front .brand {
    position: absolute; top: 46px; right: 50px;
  }
  .card--front .brand__name { color: var(--foil); }
  .card--front .brand__tagline { color: var(--muted); }
  .card--back .brand { color: var(--emboss); text-shadow: 0 1px 0 #333336; }
  .card--back .brand__name { font-size: 72px; }
  .card--back .brand__tagline { font-size: 17px; }
  .divider {
    position: absolute; left: 200px; right: 40px; top: 152px;
    height: 1px; background: var(--rule);
  }
  .contact {
    position: absolute; left: 40px; bottom: 34px;
    font-family: "Arimo", sans-serif; color: var(--text);
  }
  .contact__name {
    font-family: "Montserrat", sans-serif; font-weight: 600;
    color: var(--foil); font-size: 19px; letter-spacing: 0.3px;
  }
  .contact__role { font-size: 13px; margin-bottom: 14px; color: var(--text); }
  .contact__list { list-style: none; font-size: 12.5px; }
  .contact__list li { display: flex; align-items: center; gap: 9px; margin-top: 5px; }
  .contact__list svg { width: 14px; height: 14px; flex: none; }
  .contact__highlight { color: var(--foil); }
  .address {
    position: absolute; right: 40px; bottom: 52px;
    font-family: "Arimo", sans-serif; font-style: normal; color: var(--text);
    font-size: 12.5px; line-height: 1.45; text-align: left;
  }
</style>
</head>
<body>
<main class="canvas">
  <section class="card card--front" aria-label="Card front with contact details">
    <div class="brand">
      <div class="brand__name">TAVREL</div>
      <div class="brand__tagline">CRAFTED INTERIORS</div>
    </div>
    <div class="divider"></div>
    <div class="contact">
      <div class="contact__name">ELENA MARWICK</div>
      <div class="contact__role">Managing Director</div>
      <ul class="contact__list">
        <li>
          <svg viewBox="0 0 16 16" aria-hidden="true"><rect x="1" y="1" width="14" height="14" rx="2" fill="none" stroke="#c9a063" stroke-width="1.4"/><path d="M5 4.5l1.6 0 .8 2-1 .8a6 6 0 0 0 2.3 2.3l.8-1 2 .8v1.6c-3.6.4-6.9-2.9-6.5-6.5z" fill="#c9a063"/></svg>
          041-582 307 964
        </li>
        <li>
          <svg viewBox="0 0 16 16" aria-hidden="true"><rect x="1" y="3" width="14" height="10" fill="#c9a063"/><path d="M1 3l7 6 7-6M1 13l5-5M15 13l-5-5" fill="none" stroke="#2a2a2d" stroke-width="1.2"/></svg>
          hello@tavrelstudio.com
        </li>
        <li>
          <svg viewBox="0 0 16 16" aria-hidden="true"><circle cx="8" cy="8" r="6.8" fill="#c9a063"/><path d="M1.5 8h13M8 1.2v13.6M3 4.5h10M3 11.5h10M8 1.2c-3.2 3.6-3.2 10 0 13.6M8 1.2c3.2 3.6 3.2 10 0 13.6" fill="none" stroke="#2a2a2d" stroke-width="0.9"/></svg>
          <span>www.<span class="contact__highlight">tavrelstudio</span>.com</span>
        </li>
      </ul>
    </div>
    <address class="address">
      18, Harlow Lane Studios<br>
      Brightwater, 40871
    </address>
  </section>

  <section class="card card--back" aria-label="Card back with brand name">
    <div class="brand">
      <div class="brand__name">TAVREL</div>
      <div class="brand__tagline">CRAFTED INTERIORS</div>
    </div>
  </section>
</main>
</body>
</html>
```